Rovilent.com Trucking Company Website

Need a website designed (no content) for a trucking company, specializing in trucking of ocean containers (intermodal Trucking). Heavy emphasis on technology, using latest technology, providing unabated visibility and realtime information.
clean minimalist industrial website
example:
https://www.belquarn.com/

Target Market(s)

Professional Business Consumer corporate and small business

Industry/Entity Type

Trucking Company

Number of Pages Required

5+ page

Requirements
Must have
• Industrial Design, simple informative, for a busy professional to view and get the necessary information with out the distractions.
• Blog Page
• Client Log-In on the front page
• Technology page - showing our intensive investments in technology
Nice to have
• If ANY images included, MUST be USA related. Example if include an image of a truck, ensure its a USA model. Do the research.
• included our business card for sample of Logo
• Doesnt not have to be the same color schemes.
Should not have
• moving images

```html
<!DOCTYPE html>
<html lang="en">
<head>
<meta charset="utf-8">
<title>Rovilent – Blog</title>
<link href="https://fonts.googleapis.com/css2?family=Open+Sans:wght@400;600;700&display=swap" rel="stylesheet">
<style>
:root{
  --blue:#1b8ad3;
  --orange:#f39019;
  --ink:#3b3f44;
  --text:#7a7f85;
  --rule:#e3e5e8;
  --tag:#eeeff1;
  --white:#ffffff;
}
*{box-sizing:border-box;margin:0;padding:0}
html,body{width:1200px;height:4276px;overflow:hidden}
body{position:relative;background:var(--white);font-family:"Open Sans",Arial,sans-serif;color:var(--ink)}
.abs{position:absolute}

/* hero */
.hero{left:0;top:0;width:1200px;height:556px;background:linear-gradient(100deg,#3d5566 0%,#a7743f 28%,#6a3b2c 48%,#8e2a22 70%,#3a1a1a 100%)}
.hero-shade{left:0;top:0;width:1200px;height:556px;background:linear-gradient(180deg,rgba(20,30,40,.35) 0%,rgba(0,0,0,0) 40%,rgba(0,0,0,.35) 100%)}
.topbar{left:0;top:0;width:1200px;height:48px;background:rgba(28,44,58,.8)}
.field{top:11px;height:26px;background:rgba(255,255,255,.9);border-radius:2px;font-size:11px;color:#8a9099;padding:5px 10px}
.login{left:433px;top:11px;width:66px;height:26px;background:var(--orange);color:#fff;font-size:11px;font-weight:700;text-align:center;line-height:26px;border-radius:2px}
.contact-mini{top:8px;color:#fff;font-size:11px;line-height:15px}
.contact-mini b{display:block;font-weight:700}
.hire{left:963px;top:0;width:237px;height:48px;background:var(--orange);color:#fff;font-weight:700;font-size:15px;letter-spacing:.5px;text-align:center;line-height:48px}
.logo{left:74px;top:66px;color:#fff;font-weight:700;font-size:30px;letter-spacing:1px}
.nav a{position:absolute;top:78px;color:#fff;font-size:13px;text-decoration:none;letter-spacing:.3px}
.nav-active{left:920px;top:108px;width:76px;height:3px;background:var(--blue)}
.hero-title{left:72px;top:372px;color:#fff;font-size:48px;font-weight:700}
.hero-sub{left:74px;top:436px;color:#fff;font-size:15px;line-height:26px}

/* posts */
.post-title{left:74px;width:781px;text-align:center;font-size:33px;font-weight:400;letter-spacing:2px;color:var(--ink);line-height:43px}
.post-rule{left:420px;width:90px;height:4px;background:var(--blue)}
.post-date{left:74px;width:781px;text-align:center;font-size:13px;font-weight:700;letter-spacing:1px;color:var(--ink)}
.post-text{left:74px;width:781px;font-size:13.5px;line-height:23px;color:var(--text)}
.more{left:74px;width:781px;text-align:center;font-size:12px;font-weight:700;letter-spacing:1.5px;color:var(--ink)}
.share{left:74px;width:781px;border-top:1px solid var(--rule);border-bottom:1px solid var(--rule)}
.share-split{position:absolute;left:391px;top:0;bottom:0;width:1px;background:var(--rule)}
.comments{position:absolute;left:134px;font-size:13px;color:var(--text)}
.comments b{color:var(--ink);margin-right:14px}
.dots{position:absolute;left:508px;display:flex;gap:26px}
.dots span{width:14px;height:14px;border-radius:50%;background:#6d737a}
.pager{top:3910px;font-size:12px;font-weight:700;letter-spacing:1.5px;color:var(--ink)}

/* sidebar */
.side-head{left:884px;width:256px;height:46px;background:var(--blue);color:#fff;font-size:13px;font-weight:700;letter-spacing:1px;text-align:center;line-height:46px}
.thumb{width:77px;height:77px}
.tags{left:884px;top:1086px;width:256px;display:flex;flex-wrap:wrap;gap:5px}
.tags span{background:var(--tag);border:1px solid #dadde1;font-size:9.5px;color:#6d737a;padding:3px 8px;letter-spacing:.3px}
.latest{left:884px;width:256px}
.latest .pic{position:absolute;left:0;top:0;width:62px;height:57px}
.latest h4{position:absolute;left:88px;top:0;width:168px;font-size:12px;font-weight:400;letter-spacing:1px;line-height:16px;color:var(--ink)}
.latest p{position:absolute;left:88px;font-size:9.5px;color:var(--text);letter-spacing:.5px}

/* footer */
.footer{left:0;top:3998px;width:1200px;height:183px;background:var(--blue);color:#fff}
.footer h3{position:absolute;left:74px;top:72px;font-size:27px;font-weight:700;letter-spacing:1px}
.footer .bar{position:absolute;left:74px;top:115px;width:64px;height:4px;background:var(--orange)}
.footer .note{position:absolute;left:74px;top:140px;font-size:14px;font-weight:700}
.fcol{position:absolute;top:70px;font-size:13px;line-height:26px}
.fcol b{display:block;font-size:14px;line-height:22px}
.fcol div{display:flex;align-items:center;gap:12px}
.fbtn{position:absolute;left:1012px;width:114px;height:28px;border:2px solid #fff;border-radius:14px;font-size:10px;font-weight:700;text-align:center;line-height:24px}
.copy{left:0;top:4181px;width:1200px;height:95px;background:var(--orange);color:#fff;font-size:13px;font-weight:700;padding:24px 74px;line-height:22px}
</style>
</head>
<body>

<!-- header / hero -->
<div class="abs hero" role="img" aria-label="Photo of a red trailer truck on a highway at sunset"></div>
<div class="abs hero-shade"></div>
<div class="abs topbar"></div>
<div class="abs field" style="left:74px;width:168px">Username</div>
<div class="abs field" style="left:254px;width:165px">Password</div>
<div class="abs login">LOGIN</div>
<svg class="abs" style="left:610px;top:12px" width="22" height="22" viewBox="0 0 24 24"><path d="M6.6 10.8a15 15 0 0 0 6.6 6.6l2.2-2.2c.3-.3.7-.4 1-.2 1.1.4 2.3.6 3.6.6.6 0 1 .4 1 1V20c0 .6-.4 1-1 1A17 17 0 0 1 3 4c0-.6.4-1 1-1h3.5c.6 0 1 .4 1 1 0 1.3.2 2.5.6 3.6.1.3 0 .7-.2 1z" fill="#fff"/></svg>
<div class="abs contact-mini" style="left:646px"><b>Phone</b>(+00) 000 000</div>
<svg class="abs" style="left:792px;top:12px" width="26" height="22" viewBox="0 0 26 22"><rect x="1.5" y="2.5" width="23" height="17" fill="none" stroke="#fff" stroke-width="2"/><path d="M2 3l11 9 11-9" fill="none" stroke="#fff" stroke-width="2"/></svg>
<div class="abs contact-mini" style="left:832px"><b>Email</b>info@rovilent.com</div>
<div class="abs hire">HIRE A TRUCK</div>

<div class="abs logo">ROVILENT</div>
<nav class="nav">
  <a style="left:490px">HOME</a>
  <a style="left:584px">ABOUT US</a>
  <a style="left:706px">SERVICES</a>
  <a style="left:822px">CONTACT</a>
  <a style="left:935px">BLOG</a>
  <a style="left:1030px">TECHNOLOGY</a>
</nav>
<div class="abs nav-active"></div>
<h1 class="abs hero-title">Suspendisse Potenti</h1>
<p class="abs hero-sub">Vestibulum eget pharetra magna, a consequat lectus.<br>Vestibulum volutpat interdum dolor ex interdum.</p>

<!-- post 1 -->
<h2 class="abs post-title" style="top:618px">BRAND NEW TRUCKS HAVE ARRIVED!</h2>
<div class="abs post-rule" style="top:674px"></div>
<div class="abs post-date" style="top:695px">JANUARY 13, 2017</div>
<div class="abs" style="left:305px;top:892px;width:345px;height:263px;background:linear-gradient(180deg,#e2342f,#b81f1f 70%,#3a3a3a)" role="img" aria-label="Photo of a new red box truck"></div>
<p class="abs post-text" style="top:1300px">Sed rutrum sapien eget urna vestibulum tincidunt quis non est. Quisque sit amet diam pellentesque, semper sem quis, rhoncus ex. In vel magna euismod, fringilla enim eget, elementum dolor.</p>
<p class="abs post-text" style="top:1380px">Suspendisse potenti. Phasellus venenatis hendrerit odio, eu molestie quam faucibus id. Vivamus ultricies lorem aliquam mi imperdiet, et tincidunt ex sodales. Proin nec sagittis sem, id lacinia justo. Aliquam venenatis viverra lectus, quis ullamcorper mi pulvinar id...</p>
<div class="abs more" style="top:1474px">CONTINUE READING</div>
<div class="abs share" style="top:1539px;height:105px">
  <div class="share-split"></div>
  <div class="comments" style="top:41px"><b>5</b>Comments</div>
  <div class="dots" style="top:45px"><span></span><span></span><span></span><span></span></div>
</div>

<!-- post 2 -->
<h2 class="abs post-title" style="top:1682px">TRADE ROUTE: THROUGH THE RED SEA</h2>
<div class="abs post-rule" style="top:1737px"></div>
<div class="abs post-date" style="top:1758px">JANUARY 12, 2017</div>
<div class="abs" style="left:162px;top:1847px;width:605px;height:453px;background:radial-gradient(ellipse at center,#b59a6a 0%,#8b7348 60%,#4e3f25 100%)" role="img" aria-label="Antique world map"></div>
<p class="abs post-text" style="top:2363px">Sed rutrum sapien eget urna vestibulum tincidunt quis non est. Quisque sit amet diam pellentesque, semper sem quis, rhoncus ex. In vel magna euismod, fringilla enim eget, elementum dolor.</p>
<p class="abs post-text" style="top:2432px">Suspendisse potenti. Phasellus venenatis hendrerit odio, eu molestie quam faucibus id. Vivamus ultricies lorem aliquam mi imperdiet, et tincidunt ex sodales. Proin nec sagittis sem, id lacinia justo. Aliquam venenatis viverra lectus, quis ullamcorper mi pulvinar id...</p>
<div class="abs more" style="top:2540px">CONTINUE READING</div>
<div class="abs share" style="top:2605px;height:103px">
  <div class="share-split"></div>
  <div class="comments" style="top:38px"><b>5</b>Comments</div>
  <div class="dots" style="top:42px"><span></span><span></span><span></span><span></span></div>
</div>

<!-- post 3 -->
<h2 class="abs post-title" style="top:2745px">FAQS:<br>COMMON QUESTIONS AND ANSWERS</h2>
<div class="abs post-rule" style="top:2845px"></div>
<div class="abs post-date" style="top:2870px">JANUARY 10, 2017</div>
<div class="abs" style="left:162px;top:2955px;width:605px;height:456px;background:linear-gradient(135deg,#7c6a55 0%,#9a8569 35%,#a9d8e6 55%,#e8c64a 75%,#6f5d49 100%)" role="img" aria-label="Sticky notes with a question mark on a wooden table"></div>
<p class="abs post-text" style="top:3472px">Sed rutrum sapien eget urna vestibulum tincidunt quis non est. Quisque sit amet diam pellentesque, semper sem quis, rhoncus ex. In vel magna euismod, fringilla enim eget, elementum dolor.</p>
<p class="abs post-text" style="top:3543px">Suspendisse potenti. Phasellus venenatis hendrerit odio, eu molestie quam faucibus id. Vivamus ultricies lorem aliquam mi imperdiet, et tincidunt ex sodales. Proin nec sagittis sem, id lacinia justo. Aliquam venenatis viverra lectus, quis ullamcorper mi pulvinar id...</p>
<div class="abs more" style="top:3648px">CONTINUE READING</div>
<div class="abs share" style="top:3756px;height:80px">
  <div class="share-split"></div>
  <div class="comments" style="top:30px"><b>5</b>Comments</div>
  <div class="dots" style="top:33px"><span></span><span></span><span></span><span></span></div>
</div>

<div class="abs pager" style="left:74px">&larr; NEWER POSTS</div>
<div class="abs pager" style="left:737px">OLDER POSTS &rarr;</div>

<!-- sidebar -->
<div class="abs side-head" style="top:630px">PINTEREST</div>
<div class="abs thumb" style="left:884px;top:707px;background:#c9d3dc" role="img" aria-label="White truck photo"></div>
<div class="abs thumb" style="left:973px;top:707px;background:#b8573a" role="img" aria-label="Red truck photo"></div>
<div class="abs thumb" style="left:1063px;top:707px;background:#d8d2c4" role="img" aria-label="Route map photo"></div>
<div class="abs thumb" style="left:884px;top:798px;background:#5a6d86" role="img" aria-label="Truck on highway photo"></div>
<div class="abs thumb" style="left:973px;top:798px;background:#7a5a3a" role="img" aria-label="Truck at dusk photo"></div>
<div class="abs thumb" style="left:1063px;top:798px;background:#8c7a55" role="img" aria-label="Old map photo"></div>
<div class="abs thumb" style="left:884px;top:889px;background:#4a5e78" role="img" aria-label="Truck fleet photo"></div>
<div class="abs thumb" style="left:973px;top:889px;background:#b2483a" role="img" aria-label="Parked trucks photo"></div>
<div class="abs thumb" style="left:1063px;top:889px;background:#d9b93a" role="img" aria-label="Road sign photo"></div>

<div class="abs side-head" style="top:1012px">TAGS</div>
<div class="abs tags">
  <span>MAGNA</span><span>CONSEQUAT</span><span>PHARETRA</span><span>EGET</span>
  <span>PHARETRA</span><span>MAGNA</span><span>EGET</span><span>CONSEQUAT</span>
  <span>MAGNA</span><span>CONSEQUAT</span><span>PHARETRA</span><span>EGET</span>
  <span>PHARETRA</span><span>MAGNA</span><span>EGET</span><span>CONSEQUAT</span>
  <span>ELEMENTUM</span>
</div>

<div class="abs side-head" style="top:1251px">LATEST POSTS</div>
<div class="abs latest" style="top:1325px">
  <div class="pic" style="background:#d8403a" role="img" aria-label="Red truck thumbnail"></div>
  <h4>BRAND NEW TRUCKS HAVE ARRIVED</h4><p style="top:40px">JANUARY 13, 2017</p>
</div>
<div class="abs latest" style="top:1452px">
  <div class="pic" style="background:#8b7348" role="img" aria-label="Old map thumbnail"></div>
  <h4>TRADE ROUTE: THROUGH THE RED SEA</h4><p style="top:52px">JANUARY 12, 2017</p>
</div>
<div class="abs latest" style="top:1580px">
  <div class="pic" style="background:#9bb9bd" role="img" aria-label="Sticky notes thumbnail"></div>
  <h4>FAQS: COMMON QUESTIONS AND ANSWERS</h4><p style="top:52px">JANUARY 10, 2017</p>
</div>

<!-- footer -->
<footer class="abs footer">
  <h3>CONTACT</h3>
  <div class="bar"></div>
  <div class="note">Please do not hesitate to contact us through:</div>
  <div class="fcol" style="left:433px">
    <b>Headquater</b>
    <div><svg width="14" height="14" viewBox="0 0 24 24"><path d="M6.6 10.8a15 15 0 0 0 6.6 6.6l2.2-2.2c.3-.3.7-.4 1-.2 1.1.4 2.3.6 3.6.6.6 0 1 .4 1 1V20c0 .6-.4 1-1 1A17 17 0 0 1 3 4c0-.6.4-1 1-1h3.5c.6 0 1 .4 1 1 0 1.3.2 2.5.6 3.6.1.3 0 .7-.2 1z" fill="#fff"/></svg>(+00) 000 000</div>
    <div><svg width="14" height="14" viewBox="0 0 24 24"><path d="M12 2a7 7 0 0 0-7 7c0 5 7 13 7 13s7-8 7-13a7 7 0 0 0-7-7zm0 9.5A2.5 2.5 0 1 1 12 6.5a2.5 2.5 0 0 1 0 5z" fill="#fff"/></svg>Lorem Ipsum Dolor Sit Amet, 70000</div>
    <div><svg width="14" height="12" viewBox="0 0 26 22"><rect x="1.5" y="2.5" width="23" height="17" fill="none" stroke="#fff" stroke-width="2.5"/><path d="M2 3l11 9 11-9" fill="none" stroke="#fff" stroke-width="2.5"/></svg>info@rovilent.com</div>
  </div>
  <div class="fcol" style="left:792px">
    <b>Customer Services</b>
    <div><svg width="14" height="14" viewBox="0 0 24 24"><path d="M6.6 10.8a15 15 0 0 0 6.6 6.6l2.2-2.2c.3-.3.7-.4 1-.2 1.1.4 2.3.6 3.6.6.6 0 1 .4 1 1V20c0 .6-.4 1-1 1A17 17 0 0 1 3 4c0-.6.4-1 1-1h3.5c.6 0 1 .4 1 1 0 1.3.2 2.5.6 3.6.1.3 0 .7-.2 1z" fill="#fff"/></svg>(+00) 000 000</div>
    <div><svg width="14" height="12" viewBox="0 0 26 22"><rect x="1.5" y="2.5" width="23" height="17" fill="none" stroke="#fff" stroke-width="2.5"/><path d="M2 3l11 9 11-9" fill="none" stroke="#fff" stroke-width="2.5"/></svg>cs@rovilent.com</div>
  </div>
  <div class="fbtn" style="top:98px">HOME PAGE</div>
  <div class="fbtn" style="top:140px">NEW TECHNOLOGY</div>
</footer>
<div class="abs copy">Copyright 2017, rovilent. All Rights Reserved</div>

</body>
</html>
```